International Dating Site for modern people

We need a site design for a brand new dating site. Feel free to express your ideas and creativity. The final design should be creative and positive feeling, warm.

major elements:
- main page
- login/logout (form)
- profile editing (form)
- profile page with pictures
- search page and results page (form, table)
- a message box or the header in the main page with the following theme, feeling:
winter, spring, summer, autumn, christmas, easter, new year
- blog subpage (title, content)
- menu (login/blog/search/profile/logout)
- footer (impressum, faq, contact, privacy policy)

Target Market(s)

people between 21 and 45

Industry/Entity Type

Social

Number of Pages Required

4 page

Font styles to use
Sans Serif

Requirements
Must have
• happy, positive, warm look and feel and responsive design (plan to target different devices, the final and coded version will be responsive but please think of it when you design elements)
Nice to have
• creative

```html
<!DOCTYPE html>
<html lang="en">
<head>
<meta charset="utf-8">
<title>Heartline – International Dating</title>
<link rel="stylesheet" href="https://fonts.googleapis.com/css2?family=Raleway:wght@400;600;700;800&family=Open+Sans:wght@400;600&display=swap">
<style>
:root{
  --red:#d0352a;
  --ink:#333333;
  --ink-soft:#555555;
  --muted:#888888;
  --white:#ffffff;
  --circle:#3d3d3d;
  --hero-top:#3f4d5e;
  --hero-mid:#6b6a68;
  --hero-low:#2c3440;
  --about-a:#b3200f;
  --about-b:#d9451c;
}
*{margin:0;padding:0;box-sizing:border-box}
html,body{width:1200px;height:3041px;overflow:hidden;background:var(--white)}
body{position:relative;font-family:"Open Sans",sans-serif;color:var(--ink)}
.abs{position:absolute}
.center{left:0;width:1200px;text-align:center}
.heading{font-family:"Raleway",sans-serif;font-weight:700;letter-spacing:2px;text-transform:uppercase}
.btn{position:absolute;display:flex;align-items:center;justify-content:center;background:var(--red);color:var(--white);border-radius:22px;font-family:"Raleway",sans-serif;font-weight:700;font-size:13px;letter-spacing:1px;text-transform:uppercase}

/* header */
.site-header{position:absolute;top:0;left:0;width:1200px;height:69px;background:var(--white)}
.brand{position:absolute;left:97px;top:18px;font-family:"Raleway",sans-serif;font-weight:800;font-size:25px;letter-spacing:3px;color:var(--ink)}
.nav-link{position:absolute;top:27px;font-family:"Raleway",sans-serif;font-weight:600;font-size:12.5px;letter-spacing:1px;color:var(--ink)}
.nav-cta{left:924px;top:20px;width:177px;height:34px;font-size:11.5px}

/* hero */
.hero{position:absolute;top:69px;left:0;width:1200px;height:553px;background:linear-gradient(180deg,var(--hero-top) 0%,var(--hero-mid) 45%,#574a3c 55%,var(--hero-low) 100%)}
.hero-title{top:258px;font-size:50px;color:var(--white);letter-spacing:5px}
.hero-sub{top:325px;font-family:"Raleway",sans-serif;font-size:25px;letter-spacing:2px;color:var(--white);font-weight:400}
.hero-cta{left:523px;top:379px;width:156px;height:36px}

/* welcome */
.welcome-title{top:694px;font-size:31px;color:var(--ink)}
.welcome-text{top:757px;left:170px;width:860px;text-align:center;font-size:12.5px;line-height:26.5px;color:var(--ink-soft)}
.welcome-cta{left:507px;top:859px;width:184px;height:49px;border-radius:25px;font-size:13px}

/* features */
.feature{position:absolute;top:994px;width:330px;height:120px}
.feature-icon{position:absolute;left:0;top:0;width:83px;height:83px;border-radius:50%;background:var(--circle)}
.feature-icon svg{position:absolute;left:0;top:0}
.feature-title{position:absolute;left:110px;top:8px;font-family:"Raleway",sans-serif;font-weight:700;font-size:13.5px;letter-spacing:1.5px;line-height:21px;color:var(--ink);text-transform:uppercase}
.feature-text{position:absolute;left:110px;top:54px;width:210px;font-size:11px;line-height:22px;color:var(--muted)}

/* members */
.section-title{font-size:19px;color:var(--ink)}
.rule{position:absolute;left:585px;width:30px;height:3px;background:var(--red)}
.member{position:absolute;width:300px}
.member-photo{width:300px;height:269px;background:linear-gradient(135deg,#d6ccc3,#9c8a7c 60%,#6e6259)}
.member-name{margin-top:20px;text-align:center;font-family:"Raleway",sans-serif;font-weight:700;font-size:14px;letter-spacing:1.5px;color:#666;text-transform:uppercase}
.member-age{margin-top:2px;text-align:center;font-size:10.5px;color:var(--muted)}

/* posts */
.post{position:absolute;width:470px}
.post-title{font-family:"Raleway",sans-serif;font-weight:700;font-size:14px;letter-spacing:1.5px;color:var(--ink);text-transform:uppercase}
.post-text{margin-top:12px;font-size:12.5px;line-height:26px;color:var(--muted)}

/* about */
.about{position:absolute;top:2370px;left:0;width:1200px;height:383px;background:linear-gradient(120deg,var(--about-a),var(--about-b) 50%,#a8180c)}
.about-title{top:2460px;font-size:19px;color:var(--white)}
.about-text{top:2524px;left:200px;width:800px;text-align:center;font-size:11.5px;line-height:24.5px;color:var(--white)}
.about-cta{left:517px;top:2621px;width:166px;height:40px;background:transparent;border:1px solid rgba(255,255,255,.85);font-weight:600;font-size:11.5px}

/* footer */
.footer-brand{top:2810px;font-family:"Raleway",sans-serif;font-weight:800;font-size:25px;letter-spacing:4px;color:var(--ink)}
.footer-link{position:absolute;top:2862px;font-size:14px;color:var(--ink-soft);transform:translateX(-50%)}
.copyright{top:2901px;font-size:12px;color:var(--ink-soft)}
.social{position:absolute;top:2947px;width:32px;height:32px;border-radius:50%}
</style>
</head>
<body>

<header class="site-header">
  <div class="brand">HEARTLINE</div>
  <nav>
    <span class="nav-link" style="left:422px">LOGIN</span>
    <span class="nav-link" style="left:522px">BLOG</span>
    <span class="nav-link" style="left:617px">SEARCH</span>
    <span class="nav-link" style="left:728px">PROFILE</span>
    <span class="nav-link" style="left:840px">LOGOUT</span>
    <span class="btn nav-cta">Search your favorite</span>
  </nav>
</header>

<section class="hero" role="img" aria-label="City river at sunset with a stone chain bridge and its reflection on the water"></section>
<h1 class="abs center heading hero-title">HEARTLINE</h1>
<p class="abs center hero-sub">LOREM IPSUM IS SIMPLY DUMMY TEXT OF THE PRINTING</p>
<span class="btn hero-cta">Join us now</span>

<h2 class="abs center heading welcome-title">Welcome to Heartline</h2>
<p class="abs welcome-text">Lorem Ipsum is simply dummy text of the printing and typesetting industry. Lorem Ipsum has been the industry's standard dummy text ever since the 1500s, when an unknown printer took a galley of type and scrambled it to make a type specimen book. It has survived not only five centuries, but also the leap into electronic typesetting, remaining essentially unchanged.</p>
<span class="btn welcome-cta">Subscribe here!</span>

<div class="feature" style="left:99px">
  <div class="feature-icon">
    <svg width="83" height="83" viewBox="0 0 83 83"><circle cx="44" cy="38" r="13" fill="none" stroke="#fff" stroke-width="3"/><line x1="35" y1="47" x2="26" y2="57" stroke="#fff" stroke-width="5" stroke-linecap="round"/></svg>
  </div>
  <div class="feature-title">Search your<br>favorite</div>
  <p class="feature-text">Lorem Ipsum is simply dummy text of the printing and typesetting industry. has been the industry...</p>
</div>
<div class="feature" style="left:446px">
  <div class="feature-icon">
    <svg width="83" height="83" viewBox="0 0 83 83"><rect x="24" y="38" width="8" height="20" rx="1" fill="#fff"/><path d="M35 39 L42 26 Q46 22 47 28 L45 36 H56 Q60 37 59 41 L56 54 Q55 58 51 58 H35 Z" fill="#fff"/></svg>
  </div>
  <div class="feature-title">Choose your<br>favorite</div>
  <p class="feature-text">Lorem Ipsum is simply dummy text of the printing and typesetting industry. has been the industry...</p>
</div>
<div class="feature" style="left:795px">
  <div class="feature-icon">
    <svg width="83" height="83" viewBox="0 0 83 83"><circle cx="34" cy="34" r="7" fill="#fff"/><path d="M21 56 Q22 44 34 44 Q46 44 47 56 Z" fill="#fff"/><circle cx="50" cy="32" r="7" fill="#fff"/><path d="M49 42 Q61 42 62 54 H50 Q50 46 45 43 Z" fill="#fff"/></svg>
  </div>
  <div class="feature-title">Joined with<br>your pair</div>
  <p class="feature-text">Lorem Ipsum is simply dummy text of the printing and typesetting industry. has been the industry...</p>
</div>

<h2 class="abs center heading section-title" style="top:1190px">Meet new men &amp; women</h2>

<div class="member" style="left:0;top:1267px"><div class="member-photo" role="img" aria-label="Portrait of a smiling member"></div><div class="member-name">Mira Dellano</div><div class="member-age">24 years</div></div>
<div class="member" style="left:300px;top:1267px"><div class="member-photo" role="img" aria-label="Portrait of a smiling member"></div><div class="member-name">Mira Dellano</div><div class="member-age">24 years</div></div>
<div class="member" style="left:600px;top:1267px"><div class="member-photo" role="img" aria-label="Portrait of a smiling member"></div><div class="member-name">Mira Dellano</div><div class="member-age">24 years</div></div>
<div class="member" style="left:900px;top:1267px"><div class="member-photo" role="img" aria-label="Portrait of a smiling member"></div><div class="member-name">Mira Dellano</div><div class="member-age">24 years</div></div>
<div class="member" style="left:0;top:1607px"><div class="member-photo" role="img" aria-label="Portrait of a smiling member"></div><div class="member-name">Mira Dellano</div><div class="member-age">24 years</div></div>
<div class="member" style="left:300px;top:1607px"><div class="member-photo" role="img" aria-label="Portrait of a smiling member"></div><div class="member-name">Mira Dellano</div><div class="member-age">24 years</div></div>
<div class="member" style="left:600px;top:1607px"><div class="member-photo" role="img" aria-label="Portrait of a smiling member"></div><div class="member-name">Mira Dellano</div><div class="member-age">24 years</div></div>
<div class="member" style="left:900px;top:1607px"><div class="member-photo" role="img" aria-label="Portrait of a smiling member"></div><div class="member-name">Mira Dellano</div><div class="member-age">24 years</div></div>

<h2 class="abs center heading section-title" style="top:1997px">Recent posts</h2>
<div class="rule" style="top:2032px"></div>

<article class="post" style="left:101px;top:2095px"><h3 class="post-title">Lorem ipsum is simply dummy text</h3><p class="post-text">Lorem Ipsum is simply dummy text of the printing and typesetting industry. Lorem Ipsum has been the industry...</p></article>
<article class="post" style="left:634px;top:2095px"><h3 class="post-title">Lorem ipsum is simply dummy text</h3><p class="post-text">Lorem Ipsum is simply dummy text of the printing and typesetting industry. Lorem Ipsum has been the industry...</p></article>
<article class="post" style="left:101px;top:2223px"><h3 class="post-title">Lorem ipsum is simply dummy text</h3><p class="post-text">Lorem Ipsum is simply dummy text of the printing and typesetting industry. Lorem Ipsum has been the industry...</p></article>
<article class="post" style="left:634px;top:2223px"><h3 class="post-title">Lorem ipsum is simply dummy text</h3><p class="post-text">Lorem Ipsum is simply dummy text of the printing and typesetting industry. Lorem Ipsum has been the industry...</p></article>

<section class="about" role="img" aria-label="Red-tinted photo of friends laughing and celebrating at a party"></section>
<h2 class="abs center heading section-title about-title">About Heartline</h2>
<div class="rule" style="top:2497px;background:var(--white)"></div>
<p class="abs about-text">Lorem Ipsum is simply dummy text of the printing and typesetting industry. Lorem Ipsum has been the industry's standard dummy text ever since the 1500s, when an unknown printer took a galley of type and scrambled it to make a type specimen book. It has survived not only five centuries, but also the leap into electronic typesetting, remaining essentially unchanged.</p>
<span class="btn about-cta">View more details</span>

<footer>
  <div class="abs center footer-brand">HEARTLINE</div>
  <span class="footer-link" style="left:434px">Impressum</span>
  <span class="footer-link" style="left:539px">Faq</span>
  <span class="footer-link" style="left:632px">Contact</span>
  <span class="footer-link" style="left:757px">Privacy policy</span>
  <p class="abs center copyright">Copyright © 2016. Heartline. All rights reserved.</p>
  <span class="social" style="left:501px;background:#2f5fa8"></span>
  <span class="social" style="left:543px;background:#1f6f9a"></span>
  <span class="social" style="left:584px;background:#f0a51d"></span>
  <span class="social" style="left:625px;background:#3fb0e3"></span>
  <span class="social" style="left:665px;background:#d62a22"></span>
</footer>

</body>
</html>
```